Criação de Papelaria Profissional para Advocacia e Direito
A empresa queria:
" Ribeiro Tavares Advogados é um escritório boutique de atuação diversificada (full service) "

```html
<!DOCTYPE html>
<html lang="pt-BR">
<head>
<meta charset="UTF-8">
<title>Ribeiro Tavares Advogados — Assinatura de e-mail</title>
<link rel="stylesheet" href="https://fonts.googleapis.com/css2?family=Open+Sans:wght@400;600&family=Tinos&display=swap">
<style>
  :root {
    --page-bg: #ececec;
    --card-white: #ffffff;
    --slate: #3f5566;
    --slate-dark: #34495a;
    --brand-grey: #5a6670;
    --muted-grey: #8a949c;
    --edge-shadow: #d4d7da;
    --on-slate: #ffffff;
    --on-slate-soft: #dfe5ea;
  }
  html, body {
    margin: 0;
    padding: 0;
    width: 1200px;
    height: 1200px;
    overflow: hidden;
    background: var(--page-bg);
  }
  .canvas {
    position: relative;
    width: 1200px;
    height: 1200px;
  }
  .signature-card {
    position: absolute;
    left: 108px;
    top: 367px;
    width: 984px;
    height: 333px;
    border-radius: 28px;
    overflow: hidden;
    background: var(--card-white);
    box-shadow: 0 22px 30px -18px rgba(0,0,0,0.35);
  }
  .card-panels {
    position: absolute;
    inset: 0;
    width: 984px;
    height: 333px;
  }
  .brand {
    position: absolute;
    left: 96px;
    top: 150px;
    display: flex;
    align-items: center;
    gap: 14px;
  }
  .brand-mark {
    width: 30px;
    height: 30px;
    background: var(--slate);
  }
  .brand-text {
    display: flex;
    flex-direction: column;
    align-items: flex-end;
  }
  .brand-name {
    font-family: "Open Sans", sans-serif;
    font-weight: 400;
    font-size: 38px;
    letter-spacing: 2px;
    line-height: 1;
    color: var(--brand-grey);
    text-transform: uppercase;
  }
  .brand-tagline {
    margin-top: 6px;
    font-family: "Open Sans", sans-serif;
    font-weight: 600;
    font-size: 10px;
    letter-spacing: 1px;
    color: var(--brand-grey);
  }
  .contact-block {
    position: absolute;
    right: 132px;
    top: 40px;
    text-align: right;
    color: var(--on-slate);
  }
  .person-name {
    font-family: "Tinos", serif;
    font-size: 29px;
    line-height: 1;
    margin: 0;
  }
  .person-role {
    font-family: "Tinos", serif;
    font-size: 19px;
    letter-spacing: 9px;
    margin: 6px -9px 0 0;
    line-height: 1;
  }
  .person-reg {
    font-family: "Open Sans", sans-serif;
    font-size: 14px;
    margin: 6px 0 0;
    color: var(--on-slate-soft);
  }
  .details {
    font-family: "Open Sans", sans-serif;
    font-size: 14px;
    line-height: 24px;
    color: var(--on-slate-soft);
    margin: 0;
  }
  .details-address { margin-top: 54px; }
  .details-phone { margin-top: 6px; }
  .details-web { margin-top: 12px; }
</style>
</head>
<body>
  <main class="canvas">
    <section class="signature-card" aria-label="Assinatura de e-mail">
      <svg class="card-panels" viewBox="0 0 984 333" aria-hidden="true">
        <path d="M 352 0 C 470 30, 530 150, 540 333" fill="none" stroke="var(--edge-shadow)" stroke-width="16"/>
        <path d="M 362 0 C 480 35, 540 150, 552 333 L 984 333 L 984 0 Z" fill="var(--slate)"/>
      </svg>

      <div class="brand">
        <span class="brand-mark"></span>
        <div class="brand-text">
          <span class="brand-name">Ribeiro Tavares</span>
          <span class="brand-tagline">Advogados e Consultores</span>
        </div>
      </div>

      <div class="contact-block">
        <p class="person-name">Carolina de Albuquerque Lima</p>
        <p class="person-role">ADVOGADA</p>
        <p class="person-reg">OAB/DF 31.562</p>
        <p class="details details-address">Avenida das Palmeiras, Lote 12, Bloco C, Sala 304,<br>Asa Norte, Brasília/DF, CEP 70714-020</p>
        <p class="details details-phone">Tel.: +55 61 3241-5086 | +55 61 98452-3317</p>
        <p class="details details-web">carolina.albuquerque@rtadvogados.com.br<br>www.rtadvogados.com.br</p>
      </div>
    </section>
  </main>
</body>
</html>
```